QM - menu design

Hi,

We require elegant menu design for upscale restaurant. Please find attached the logo and the menu items for your reference.

for inspiration, this is a good website: -
http://www.plivermark.com/tablefolio/about.php

We are very much open for Menu Size suggestions.

unfortunately the place is going under renovation, we don't have updated images to it. the closest look and feel to our place is http://vessora.com ..

we are also open for creative options on the shape, the styles, etc. as long as it represents the fine dine feel ...

Thanks ...
Updates

Dear All,

We wouldlike to extend our apology for not being able to provide feedbacks on everysingle design. We were extremely busy and we have multiple contests opensimultaneously which makes the process even harder.

However,we would like to thank you all for the efforts you have put into designingour menu. It is very much appreciated …

We wishyou all success in your design ventures and we are quite positive that we willbe working with many of you on many projects in the soon future. 

Thanks & Regards,

DHI Team...

 

 

 

Industry/Entity Type

Restaurant

Requirements
Must have
• Please ensure that there are 'some' images in the menu ... this is very important.
Should not have
• IMPORTANT: -

1. Please DO NOT insert any currency sign to the menu
2. Please keep the prices of the menu at the end of the menu items descriptions NOT beside the menu item names. The font of the price should be similar to the menu item description and please DO NOT bold the numbers. the prices should be subtle.

Thank you ...

```html
<!DOCTYPE html>
<html lang="en">
<head>
<meta charset="utf-8">
<title>Quill Mews Café – Sandwiches &amp; Soup</title>
<link href="https://fonts.googleapis.com/css2?family=Belleza&family=Mulish:wght@400;700&display=swap" rel="stylesheet">
<style>
  :root {
    --page: #e8c6b2;
    --panel: #e5cbbb;
    --accent: #c48a60;
    --accent-soft: #e0b394;
    --ink: #4a2a1c;
    --ink-heading: #5a3322;
    --stripe: #f6ece5;
    --badge: #ffffff;
  }
  html, body { margin: 0; padding: 0; overflow: hidden; }
  body { width: 850px; height: 1200px; background: var(--page); }
  .menu-page {
    position: relative; width: 850px; height: 1200px; overflow: hidden;
    background: var(--page); font-family: "Mulish", sans-serif; color: var(--ink);
  }
  .stripe { position: absolute; background: var(--stripe); }
  .stripe--top { left: 0; top: 19px; width: 850px; height: 9px; }
  .stripe--bottom { left: 0; top: 1173px; width: 720px; height: 9px; }

  .section-tab {
    position: absolute; background: var(--accent);
    font-family: "Belleza", sans-serif; color: var(--ink-heading);
  }
  .section-tab--sandwiches { left: 0; top: 58px; width: 354px; height: 80px; }
  .section-tab--sandwiches h2 {
    position: absolute; left: 52px; top: 20px; margin: 0;
    font-size: 35px; font-weight: 400; line-height: 1;
    padding: 0 0 4px 8px; border-bottom: 1.5px solid var(--ink-heading);
  }
  .section-tab--soup { left: 82px; top: 722px; width: 195px; height: 63px; }
  .section-tab--soup h2 {
    position: absolute; right: 22px; top: 12px; margin: 0;
    font-size: 36px; font-weight: 400; line-height: 1;
  }

  .sandwich-panel { position: absolute; left: 105px; top: 155px; width: 678px; height: 548px; background: var(--panel); }
  .side-rule { position: absolute; left: 783px; top: 155px; width: 17px; height: 850px; background: var(--accent); }
  .foot-rule { position: absolute; left: 299px; top: 1005px; width: 300px; height: 18px; background: var(--accent-soft); }

  .dish { position: absolute; }
  .dish h3 { margin: 0; font-size: 14px; font-weight: 700; line-height: 18px; }
  .dish p { margin: 0; font-size: 13.4px; font-weight: 400; line-height: 14px; }
  .dish .price { position: absolute; font-size: 13.4px; font-weight: 400; }

  .sandwich { left: 131px; width: 560px; }
  .sandwich h3 { margin-bottom: 12px; }
  .sandwich .price { right: 10px; bottom: 0; }

  .soup { left: 296px; width: 470px; }
  .soup h3 { margin-bottom: 13px; }
  .soup .price { right: 0; bottom: 0; }

  .brand-badge {
    position: absolute; left: 421px; top: 962px; width: 423px; height: 226px;
    border-radius: 50%; background: var(--badge);
    display: flex; align-items: center; justify-content: center;
  }
  .brand-name {
    font-family: "Mulish", sans-serif; font-weight: 400; color: var(--ink);
    font-size: 32px; letter-spacing: 6px; text-transform: uppercase;
  }
</style>
</head>
<body>
<main class="menu-page">
  <div class="stripe stripe--top"></div>
  <div class="stripe stripe--bottom"></div>

  <header class="section-tab section-tab--sandwiches"><h2>The Sandwiches</h2></header>
  <section class="sandwich-panel" aria-label="Sandwiches"></section>
  <div class="side-rule"></div>

  <article class="dish sandwich" style="top:176px">
    <h3>Grilled Vegetables Sandwich</h3>
    <p>with fresh Goat cheese and chives served with our<br>Homemade spicy garlic mayo.</p>
    <span class="price" style="right:12px">59</span>
  </article>
  <article class="dish sandwich" style="top:280px">
    <h3>Butterfish burger</h3>
    <p>with fresh tomato, beef bacon, grilled vegetables and béarnaise sauce.</p>
    <span class="price" style="right:8px">69</span>
  </article>
  <article class="dish sandwich" style="top:369px">
    <h3>Tataki Tuna sandwich</h3>
    <p>with red onion slices, stewed endives and black olives and sultanas pate’.</p>
    <span class="price" style="right:12px">79</span>
  </article>
  <article class="dish sandwich" style="top:458px">
    <h3>Beef sirloin steak sandwich</h3>
    <p>with grain mustard, Parmesan cheese and fresh<br>Nashi pears.</p>
    <span class="price" style="right:12px">79</span>
  </article>
  <article class="dish sandwich" style="top:547px">
    <h3>The Traditional Club sandwich</h3>
    <p>served with French fries and vegetable chips.</p>
    <span class="price" style="right:11px">69</span>
  </article>
  <article class="dish sandwich" style="top:621px">
    <h3>Chicken sandwich</h3>
    <p>with Parmesan cheese slices, sundried tomatoes and mint<br>Flavored mayo.</p>
    <span class="price" style="right:9px">69</span>
  </article>

  <header class="section-tab section-tab--soup"><h2>Soup</h2></header>

  <article class="dish soup" style="top:724px">
    <h3>Bouillabaisse</h3>
    <p>Traditional French Seafood soup, with Saffron and Estragon.</p>
    <span class="price">119</span>
  </article>
  <article class="dish soup" style="top:813px">
    <h3>Barley soup</h3>
    <p>With fresh vegetables, tomato smoothie and a hint of garlic oil.</p>
    <span class="price">49</span>
  </article>
  <article class="dish soup" style="top:902px">
    <h3>Beef chili</h3>
    <p>Served with Arabic bread, fresh guacamole and spicy black beans.</p>
    <span class="price">49</span>
  </article>

  <div class="foot-rule"></div>
  <div class="brand-badge"><span class="brand-name">Quill Mews Café</span></div>
</main>
</body>
</html>
```